OCD Educational Handout

I am looking for a designer to take the educational content I have created about Obsessive Compulsive Disorder and turn it into a nice-looking handout, including managing the font, layout, colors, images, illustrations, and diagrams. I would like the final product to be something I can email clients as a pdf, print out, as well as post on my website. I would like to have the final copy in a form that I can edit should I choose to adjust the content. I want the handout to be professional but also approachable to someone suffering from this disorder. I like the idea of little illustrations almost cartoon like. Almost like little doodles or something. I will have a series of handouts like this that I would want the same designer to help with, and continue with the same design style.

graphic design images and illustrations, and one or two

```html
<!DOCTYPE html>
<html lang="en">
<head>
<meta charset="utf-8">
<title>OCD Educational Handout</title>
<link rel="stylesheet" href="https://fonts.googleapis.com/css2?family=Bitter:ital,wght@0,600;0,700;1,600;1,700&family=Montserrat:wght@400;500;600;700&family=Poppins:wght@400;600&display=swap">
<style>
:root{
  --backdrop:#7b7b7b;
  --cream:#f6edd6;
  --paper:#fbf8f2;
  --terracotta:#a65d55;
  --terracotta-dark:#8f4a43;
  --rose:#a9544c;
  --teal:#6c9d91;
  --teal-light:#a9cbc4;
  --sand:#f2e5cb;
  --ink:#3b3430;
  --muted:#6f6660;
  --leaf:#b57165;
  --olive:#8aa89a;
  --white:#ffffff;
}
*{box-sizing:border-box;margin:0;padding:0}
html,body{width:1200px;height:4000px;overflow:hidden}
body{background:var(--backdrop);font-family:"Montserrat",sans-serif;color:var(--ink);position:relative}
.spread{position:absolute;left:120px;width:960px;height:740px;display:flex;box-shadow:0 6px 18px rgba(0,0,0,.25)}
.spread:nth-of-type(1){top:70px}
.spread:nth-of-type(2){top:850px}
.spread:nth-of-type(3){top:1630px}
.spread:nth-of-type(4){top:2410px}
.spread:nth-of-type(5){top:3190px}
.page{position:relative;width:480px;height:740px;overflow:hidden;background:var(--paper)}
.page--cream{background:var(--cream)}
.inner{padding:48px 42px 0 48px}
h2{font-family:"Bitter",serif;font-weight:700;color:var(--rose);font-size:17px;line-height:1.15;margin-bottom:8px}
h2.italic{font-style:italic}
.panel h2{color:var(--white)}
p{font-size:7.2px;line-height:1.45;color:var(--muted);margin-bottom:7px;text-align:justify}
p strong{color:var(--ink)}
.panel p{color:#f6e7e2}
.panel p strong{color:var(--white)}
.panel{padding:40px 40px 22px 42px}
.panel--terracotta{background:var(--terracotta)}
.panel--teal{background:var(--teal)}
.art{display:block;border-radius:50% 46% 40% 52%}
.footer{position:absolute;left:36px;right:36px;bottom:14px;display:flex;align-items:center;gap:8px;font-size:7.5px;color:var(--ink)}
.footer .mark{width:18px;height:18px;border-radius:50%;background:var(--teal-light)}
.footer .brand{font-size:5px;color:var(--muted)}
.footer .web{margin-left:auto}
.footer .pill{background:var(--teal);color:var(--white);border-radius:8px;padding:2px 8px;font-size:7px}
.checklist{list-style:none}
.checklist li{position:relative;padding-left:13px;font-size:7px;line-height:1.45;color:var(--muted);margin-bottom:5px}
.checklist li::before{content:"";position:absolute;left:0;top:2px;width:7px;height:7px;border:1px solid currentColor;border-radius:50%}
.checklist li b{color:var(--rose);font-weight:600}
.panel .checklist li{color:#eef5f2}
.card{display:flex;align-items:center;gap:10px;margin-bottom:9px}
.num{flex:none;width:26px;height:26px;border-radius:50%;border:2px solid var(--teal);color:var(--teal);font-size:10px;font-weight:600;display:flex;align-items:center;justify-content:center;background:var(--paper)}
.card-body{flex:1;background:var(--sand);border-radius:14px;padding:9px 12px;display:flex;gap:10px;align-items:center}
.card-body h3{font-size:8px;color:var(--teal);font-weight:600;margin-bottom:3px}
.card-body p{margin:0;font-size:6.6px}
.card-art{flex:none;width:62px;height:62px;border-radius:50%;background:linear-gradient(135deg,#cfe0ea,#f1c9b3)}
.leaf{position:absolute}
</style>
</head>
<body>

<!-- Cover -->
<section class="spread">
  <div class="page page--cream">
    <svg class="leaf" style="left:0;top:0" width="90" height="70" viewBox="0 0 90 70" role="img" aria-label="Decorative leaf"><path d="M0 0h60C50 30 30 55 0 62z" fill="var(--leaf)"/></svg>
    <div style="position:absolute;left:60px;top:240px;width:160px;height:160px;border-radius:50%;background:var(--terracotta);padding:6px">
      <div role="img" aria-label="Portrait photo of the therapist" style="width:100%;height:100%;border-radius:50%;background:linear-gradient(160deg,#c9c3b8,#5e5a57)"></div>
    </div>
    <div style="position:absolute;left:238px;top:236px;width:210px">
      <h2 style="font-size:21px;margin-bottom:6px">CBT for Anxiety,<br>OCD, and<br>Depression</h2>
      <div style="font-size:9px;font-weight:700;margin-bottom:10px">Boulder, CO and Beyond</div>
      <p style="text-align:left;font-size:7.4px">CBT for Anxiety, OCD, and Depression<br>Boulder, CO and Beyond<br>Living each day with anxiety, OCD, or depression can feel like you're battling a relentless storm within your own mind. You may find yourself just barely treading water, struggling to be present amidst a whirlwind of 'what ifs,' intrusive thoughts, and pervasive fear. Depression adds to the burden, casting a shadow of sadness and apathy that weighs heavily on your shoulders, making even basic tasks seem monumental.</p>
    </div>
    <div style="position:absolute;left:84px;top:555px;display:flex;flex-direction:column;align-items:center;gap:4px">
      <div style="width:58px;height:58px;border-radius:50%;background:var(--teal-light)"></div>
      <div style="font-size:7px;color:var(--ink);font-weight:600">Calm Path Therapy</div>
    </div>
    <div style="position:absolute;left:238px;top:585px;font-size:8px;line-height:2">
      <div style="font-weight:700;font-size:8.5px;margin-bottom:4px">Daniel Mercer, LCSW</div>
      <div>✉&nbsp; daniel@calmpaththerapy.com</div>
      <div>⊕&nbsp; www.calmpaththerapy.com</div>
      <div>✆&nbsp; 555-014-2290</div>
    </div>
    <div style="position:absolute;left:110px;bottom:42px;font-family:'Poppins',sans-serif;font-size:22px">www.<b style="font-weight:600">calmpaththerapy</b>.com</div>
  </div>
  <div class="page page--cream">
    <svg class="leaf" style="right:0;top:0" width="90" height="110" viewBox="0 0 90 110" role="img" aria-label="Decorative fern"><path d="M90 0v30C70 50 55 80 40 110 45 70 60 30 90 0z" fill="var(--leaf)"/></svg>
    <div style="position:absolute;left:200px;top:50px;display:flex;flex-direction:column;align-items:center;gap:4px">
      <div style="width:70px;height:70px;border-radius:50%;background:var(--teal-light)"></div>
      <div style="font-size:8px;font-weight:600">Calm Path Therapy</div>
    </div>
    <div class="art" role="img" aria-label="Illustration of a head profile with a tangled mind and small figures untangling gears" style="position:absolute;left:40px;top:160px;width:400px;height:210px;background:linear-gradient(120deg,#d6e4ec,#f3b48e 55%,#c9574b)"></div>
    <div style="position:absolute;left:0;right:0;top:430px;text-align:center">
      <div style="font-family:'Bitter',serif;font-weight:700;color:var(--teal);font-size:72px;line-height:1">OCD</div>
      <div style="font-family:'Bitter',serif;font-weight:700;color:var(--rose);font-size:28px;line-height:1.15;margin-top:4px">Obsessive Compulsive<br>Disorder</div>
      <div style="font-family:'Bitter',serif;font-size:28px;letter-spacing:1px;margin-top:4px">EDUCATIONAL</div>
    </div>
    <div style="position:absolute;left:90px;bottom:42px;font-family:'Poppins',sans-serif;font-size:22px">www.<b style="font-weight:600">calmpaththerapy</b>.com</div>
  </div>
</section>

<!-- Spread 1 -->
<section class="spread">
  <div class="page">
    <div class="inner">
      <h2>Welcome to Your First Step<br>Towards Freedom from OCD</h2>
      <p>You've just embarked on an important journey—a journey towards understanding, managing, and reclaiming your life from Obsessive-Compulsive Disorder (OCD). The first and most crucial step on this path is to learn about and study OCD itself.</p>
      <p>Understanding OCD is akin to mapping the terrain of an unfamiliar landscape. Just as a map provides insight into the terrain ahead, equipping you with knowledge about OCD empowers you to navigate your journey with greater awareness, insight and preparedness. By learning about the nature of obsessions and compulsions, the mechanisms that fuel the OCD cycle, and the various forms OCD can take, you're arming yourself with the tools needed to begin dismantling the power that OCD has over your life.</p>
      <p>This initial step is not just about acquiring information; it's about transforming that knowledge into strength, and eventually, into a strategic game plan. The first step is about shifting from a stance of feeling overwhelmed and controlled by OCD, to one of curiosity, openness and empowerment.</p>
      <p>Taking this first step by choosing to learn about OCD is a testament to your resilience and your commitment to your well-being. It marks the beginning of your journey towards freedom from OCD's grip. As you proceed through this information, keep in mind that every piece of information you gather is a tool in your arsenal against OCD, a step towards understanding your opponent, and ultimately, a step towards victory. Revisit this material as often as needed. OCD can be confusing, and even after years of helping individuals recover from OCD, I still have to remind myself of the basic fundamentals every now and again.</p>
      <p>Take notes and write down questions. Bring them with you to your next session. There are no dumb questions. The more you understand your own OCD symptoms, the better.</p>
    </div>
    <div class="art" role="img" aria-label="Illustration of a person on a ladder watering flowers growing from a large head" style="position:absolute;left:100px;top:520px;width:260px;height:170px;background:linear-gradient(120deg,#9ec3dd,#e98a6f 60%,#f6c6a6)"></div>
    <div class="footer"><span class="mark"></span><span class="brand">Calm Path</span><span class="web">www.calmpaththerapy.com</span><span class="pill">Page 01</span></div>
  </div>
  <div class="page">
    <div class="panel panel--terracotta" style="height:395px">
      <h2>What is OCD?</h2>
      <p>Obsessive-Compulsive Disorder (OCD) is a common, chronic mental health condition characterized by distressing, persistent thoughts (obsessions) and repetitive behaviors or mental acts (compulsions) that an individual feels compelled to perform. <strong>OCD is a relatively common mental health condition affecting an estimated 2–3% of the population.</strong> The age of onset ranges from early childhood through adulthood. Most common onset age is between 12–24 years old. Males generally develop the disorder between ages 13–15, while the average female onset is a bit later from ages 20–24. Among adults, the prevalence of OCD is equal for men and women. Onset of OCD is most often gradual, although in some cases acute onset has been reported.</p>
      <p><strong>Without treatment the course of OCD is chronic, with varying and changing degrees of severity over time.</strong> The chronic nature of OCD means that without treatment, symptoms are likely to progress and worsen as time goes on.</p>
      <p>OCD has a significant impact on one's life. Dealing with obsessions and compulsions for hours each day leads to severe personal distress and interferes with employment, relationships, and daily activities. <strong>Between 80% and 100% report significant difficulties</strong> and impairment in home, work, relationships, and social life.</p>
      <div style="display:flex;align-items:center;gap:14px;margin-top:8px">
        <svg width="36" height="36" viewBox="0 0 36 36" aria-label="80 percent"><circle cx="18" cy="18" r="15" fill="none" stroke="#c98c84" stroke-width="4"/><circle cx="18" cy="18" r="15" fill="none" stroke="#fff" stroke-width="4" stroke-dasharray="75.4 94.2" transform="rotate(-90 18 18)"/><text x="18" y="21" text-anchor="middle" font-size="9" font-weight="700" fill="#fff" font-family="Montserrat">80%</text></svg>
        <svg width="170" height="22" viewBox="0 0 170 22" aria-label="Eight in ten people">
          <g fill="#fff">
            <circle cx="8" cy="5" r="4"/><rect x="2" y="10" width="12" height="11" rx="5"/>
            <circle cx="28" cy="5" r="4"/><rect x="22" y="10" width="12" height="11" rx="5"/>
            <circle cx="48" cy="5" r="4"/><rect x="42" y="10" width="12" height="11" rx="5"/>
            <circle cx="68" cy="5" r="4"/><rect x="62" y="10" width="12" height="11" rx="5"/>
            <circle cx="88" cy="5" r="4"/><rect x="82" y="10" width="12" height="11" rx="5"/>
            <circle cx="108" cy="5" r="4"/><rect x="102" y="10" width="12" height="11" rx="5"/>
          </g>
          <g fill="#c98c84">
            <circle cx="128" cy="5" r="4"/><rect x="122" y="10" width="12" height="11" rx="5"/>
            <circle cx="148" cy="5" r="4"/><rect x="142" y="10" width="12" height="11" rx="5"/>
          </g>
        </svg>
      </div>
    </div>
    <div class="inner" style="padding-top:26px">
      <h2>How Does OCD<br>Operate in the Brain?</h2>
      <p style="width:200px;text-align:left">Research suggests that OCD involves communication issues between different parts of the brain, including the amygdala, which plays a key role in processing emotions. The amygdala is responsible for regulating fear and is the center of the fight or flight system. OCD can be conceptualized as a malfunctioning alarm system. Imagine a fire alarm going off when there is no actual fire. In those with OCD, the amygdala may signal that something is wrong or threatening even when there is no real danger. This can trigger the obsessive-compulsive cycle, as the brain gets stuck on these false alarms, leading to intense anxiety and the compulsive behaviors that are characteristic of OCD.</p>
    </div>
    <div class="art" role="img" aria-label="Illustration of a brain being watered with small figures seated beside it" style="position:absolute;left:265px;top:505px;width:190px;height:150px;background:linear-gradient(130deg,#bcd7e0,#f0a38c 55%,#d9e6c9)"></div>
    <div class="footer"><span class="mark"></span><span class="brand">Calm Path</span><span class="web">www.calmpaththerapy.com</span><span class="pill">Page 02</span></div>
  </div>
</section>

<!-- Spread 2 -->
<section class="spread">
  <div class="page">
    <div class="inner">
      <h2>How are Obsessions Experienced?</h2>
      <p style="margin-bottom:12px">Obsessions can vary widely in their content and impact, affecting individuals in many different ways.</p>
      <div class="card"><span class="num">01</span><div class="card-body"><div><h3>Intrusive thoughts:</h3><p>These are unwanted, recurrent thoughts and ideas that pop into a person's mind. They can be about anything, but are always unsettling and result in some kind of emotional distress. They often target a person's sense of self, threatening some pending catastrophe, or involve something terrible happening.</p></div><span class="card-art" role="img" aria-label="Illustration of a person at a desk lost in thought"></span></div></div>
      <div class="card"><span class="num">02</span><div class="card-body"><div><h3>Intrusive images:</h3><p>These are unwanted, recurrent images that pop into a person's awareness. They are experienced in the mind's eye vs. the actual eye. They can be about anything, but are always unsettling and result in some form of emotional distress.</p></div><span class="card-art" role="img" aria-label="Illustration of a worried person surrounded by images"></span></div></div>
      <div class="card"><span class="num">03</span><div class="card-body"><div><h3>Intrusive urges:</h3><p>These are sensations and feelings within the body and mind that one concludes are urges to act on an unwanted impulse. It should be noted that the individual has no true desire to act on the urge, however the urge itself is frightening to the individual.</p></div><span class="card-art" role="img" aria-label="Illustration of a person reaching toward a screen"></span></div></div>
      <div class="card"><span class="num">04</span><div class="card-body"><div><h3>Intrusive sensations</h3><p>These are unwanted sensations in the body, or a hyper awareness to normal automatic processes such as heartbeat, vision, swallowing, blinking, breathing etc. These can also include sensations in the body that feel "not right" or "off" in some way.</p></div><span class="card-art" role="img" aria-label="Illustration of a person holding their head"></span></div></div>
      <div class="card"><span class="num">05</span><div class="card-body"><div><h3>Intrusive feelings:</h3><p>Intrusive sudden experiences of fear, guilt, shame, doom, panic, and disgust etc. (despite there being no apparent or objective reason for the feeling).</p></div><span class="card-art" role="img" aria-label="Illustration of a distressed person with hands raised"></span></div></div>
    </div>
    <div class="footer"><span class="mark"></span><span class="brand">Calm Path</span><span class="web">www.calmpaththerapy.com</span><span class="pill">Page 03</span></div>
  </div>
  <div class="page">
    <div class="panel panel--teal" style="height:375px">
      <h2>What Are Compulsions?</h2>
      <p>Compulsions, or sometimes referred to as rituals, are repetitive behaviors or mental acts that an individual with Obsessive-Compulsive Disorder (OCD) feels driven to perform in response to an obsession or according to rigidly applied rules. The primary function of compulsions is to reduce emotional distress or prevent some feared outcome or situation; however, these compulsions are not realistically connected to what they are designed to neutralize or prevent, or they are deemed to be excessive and very time consuming.</p>
      <ul class="checklist">
        <li>Compulsions and Rituals are an attempt to cope and manage the intense anxiety and distress caused by the obsessions. They are an attempt to neutralize the fear and/or prevent a feared outcome.</li>
        <li>They offer temporary relief, although it is short lived. Often, once a compulsion is completed, the person feels compelled to repeat it again and again. The more compulsions a person does, the stronger the OCD gets in the long term.</li>
        <li>Compulsions often become more complex and more time consuming as the disorder progresses. Maybe a person only had to wash their hands for 30 seconds at first, but two months later they must wash for 12 minutes. Or maybe a person only had to say one prayer after having a scary thought, but after several months they must repeat it 20 times to get the same relief.</li>
        <li>Compulsions are not automatic, they are a voluntary attempt to reduce distress and prevent a feared outcome. Despite a person feeling compelled to perform the compulsion, they are still within a person's control. Whereas Obsessions (intrusive thoughts) are completely outside a person's control.</li>
        <li>Reducing and eventually eliminating compulsions is an important part of treatment, and what eventually breaks the OCD cycle and leads to long term relief.</li>
      </ul>
    </div>
    <div class="inner" style="padding-top:20px">
      <h2>Physical Compulsions</h2>
      <ul class="checklist">
        <li><b>Washing:</b> Excessive cleaning of hands/body to remove germs, contaminants, or to relieve anxiety about contamination.</li>
        <li><b>Checking:</b> Repeatedly verifying doors are locked, appliances are off, or re-reading emails to ensure no mistakes. Checking is one of the most common compulsions and can appear in many different forms.</li>
        <li><b>Ordering/Arranging:</b> Needing items to be placed in a specific order or symmetry to relieve discomfort. This can also include arranging items, clothing, body, etc until it "feels right."</li>
        <li><b>Repeating actions:</b> Opening and closing doors, tapping, re-walking steps, or rewriting words until it feels "just right," or the intrusive thought has been neutralized.</li>
        <li><b>Touching/Tapping:</b> Touching objects a certain number of times or in a specific pattern to prevent anxiety or a feared outcome. This can coincide with counting compulsions.</li>
        <li><b>Reassurance Seeking:</b> Repeatedly seeking reassurance from others whether overtly or covertly. This seeks to temporarily "wash away" doubt and fear. This can also look like researching for answers on the internet, reviewing different forums, or excessive doctor visits.</li>
      </ul>
    </div>
    <div class="footer"><span class="mark"></span><span class="brand">Calm Path</span><span class="web">www.calmpaththerapy.com</span><span class="pill">Page 04</span></div>
  </div>
</section>

<!-- Spread 3 -->
<section class="spread">
  <div class="page">
    <div class="inner">
      <h2>Mental Compulsions</h2>
      <p>Mental Compulsions are internal acts that people perform in their minds, such as counting, praying, repeating words silently, replacing a bad thought with a good thought, reviewing a memory, checking and monitoring feelings and thoughts, or performing mental rituals to counteract obsessions or to prevent perceived harm.</p>
      <ul class="checklist">
        <li><b>Counting:</b> Repeatedly counting to a certain number to prevent a bad event.</li>
        <li><b>Praying:</b> Engaging in prayer rituals to counteract negative thoughts or prevent harm. Repeating words or phrases: Silently saying words, phrases, or prayers to neutralize anxiety.</li>
        <li><b>Reviewing:</b> Mentally going over events to ensure nothing bad happened. Or replaying conversations, or reviewing how you feel about something over and over again.</li>
        <li><b>Canceling or Neutralizing:</b> Thinking a "good" thought to cancel out a "bad" thought. Or replacing a scary image with a happy image.</li>
        <li><b>List-making:</b> Creating lists to make sure important details are not forgotten or to prevent disaster. Or creating a mental list as to why something is okay, then mentally reviewing that list to reassure yourself.</li>
        <li><b>Mental Checking:</b> Checking other's responses and facial expressions, checking one's own internal feelings and responses to a particular situation or thought.</li>
        <li><b>Ruminating (see below)</b></li>
      </ul>
      <h2 style="margin-top:10px">Rumination as a Compulsion</h2>
      <p>Rumination, in the context of Obsessive-Compulsive Disorder (OCD), refers to the compulsive process of engaging in prolonged, repetitive thinking about a theme or question related to one's obsessions. Unlike productive problem-solving, ruminating in OCD does not lead to a solution or relief; instead, it exacerbates the cycle of anxiety and compulsive behavior. It is a mental compulsion that individuals with OCD often use in an attempt to resolve or make sense of their intrusive thoughts, but this strategy inevitably becomes a part of the disorder's self-perpetuating cycle. Rumination can have a profound impact on an individual's emotional well-being and quality of life. It can lead to increased anxiety, depression, and feelings of hopelessness, as the individual feels trapped in a cycle of endless thought without escape.</p>
      <ul class="checklist">
        <li><b>Intrusive and Unwanted:</b> Rumination is often experienced as intrusive and unwanted, much like the initial obsessions that trigger it.</li>
        <li>Individuals may spend hours ruminating over a single thought or question, significantly impacting their daily functioning.</li>
        <li>Continually thinking about whether one's actions have caused harm to others, despite no evidence to support this.</li>
        <li>Endlessly questioning one's moral character or integrity based on intrusive thoughts.</li>
        <li>Obsessively pondering over the meaning of life, death, or existence in a way that is distressing and unproductive.</li>
      </ul>
    </div>
    <div class="footer"><span class="mark"></span><span class="brand">Calm Path</span><span class="web">www.calmpaththerapy.com</span><span class="pill">Page 05</span></div>
  </div>
  <div class="page">
    <div class="panel panel--terracotta" style="height:265px">
      <h2>The Role of Avoidance in OCD</h2>
      <p>Avoidance plays a crucial role in the maintenance and exacerbation of Obsessive-Compulsive Disorder (OCD) by serving as a maladaptive coping strategy to minimize exposure to feared thoughts, objects, situations, or sensations. Individuals with OCD often engage in avoidance behaviors to reduce the anxiety and distress associated with their obsessions. For example, someone with contamination fears might avoid public spaces, touching door handles, or shaking hands to prevent exposure to perceived germs. Although avoidance can provide temporary relief from anxiety, it reinforces the belief in the danger of the avoided stimuli and prevents individuals from learning that their fears are often unfounded or exaggerated. This reinforcement cycle keeps the person trapped in the disorder, as avoidance behaviors become increasingly restrictive and limit one's ability to function in daily life. Furthermore, avoidance deprives individuals of the opportunity for habituation and the natural reduction of anxiety over time, making it a counterproductive strategy that sustains and can even intensify the OCD cycle.</p>
    </div>
    <div class="inner" style="padding-top:22px">
      <h2>The OCD Cycle Explained</h2>
      <p>The OCD cycle is a distressing loop that begins with intrusive, unwanted obsessions that trigger intense anxiety or discomfort. In an attempt to alleviate this distress, individuals engage in compulsive behaviors or mental acts, which are repetitive and often ritualistic actions aimed at neutralizing the obsession or preventing a feared event. Although these compulsions provide temporary relief from anxiety, this relief is short-lived and inadvertently reinforces the obsession, making the individual more likely to engage in the compulsive behavior again when the obsession reoccurs. This cycle—obsession leading to anxiety, followed by compulsive behavior and temporary relief—becomes a self-perpetuating loop that can significantly impair daily functioning and quality of life.</p>
    </div>
    <div role="img" aria-label="Hand-drawn doodle diagram of the OCD cycle linking obsession, distress, compulsion and relief with surrounding triggers such as urges, images, memories, avoidance and reassurance seeking" style="position:absolute;left:70px;top:470px;width:340px;height:210px;border-radius:30px;background:radial-gradient(circle at 50% 50%,#f4eee2 0 35%,#e9ddd0 60%,#f7f3ec 100%)"></div>
    <div class="footer"><span class="mark"></span><span class="brand">Calm Path</span><span class="web">www.calmpaththerapy.com</span><span class="pill">Page 06</span></div>
  </div>
</section>

<!-- Spread 4 -->
<section class="spread">
  <div class="page">
    <svg class="leaf" style="left:0;bottom:70px" width="40" height="60" viewBox="0 0 40 60" role="img" aria-label="Decorative leaf"><path d="M0 0C30 10 40 40 20 60L0 55z" fill="var(--olive)"/></svg>
    <div class="inner">
      <h2 class="italic">Common OCD Themes and Subtypes</h2>
      <p>While there are several well-recognized categories of OCD, such as contamination fears, harm obsessions, symmetry and ordering compulsions, and intrusive thoughts of a sexual, religious, or violent nature, it's crucial to understand that the actual spectrum of OCD themes is as varied as the individuals themselves. These themes often center around an individual's core fears and values, making the obsessions particularly distressing and the compulsions seemingly necessary for emotional survival. For instance, a person who values family above all else may experience intense fears of harm coming to loved ones, while someone who places a high value on morality might struggle with intrusive thoughts that challenge their moral or religious beliefs. This personalization of themes means that OCD can latch onto virtually any aspect of a person's life, making it a highly individualized disorder.</p>
      <ul class="checklist">
        <li><b>Contamination:</b> Fear of germs, dirt, or becoming ill from contact with people, objects, or environments. This can lead to excessive washing and cleaning behaviors.</li>
        <li><b>Harm:</b> Fear of causing harm to oneself or others through negligence or accidental actions. This often results in checking behaviors, such as repeatedly ensuring the stove is off or the door is locked.</li>
        <li><b>Symmetry and Order:</b> A need for things to be symmetrical or arranged in a specific way, leading to arranging, ordering, and repeating behaviors until things feel 'just right.'</li>
        <li><b>Sexual Intrusive Thoughts:</b> Unwanted, intrusive thoughts or images regarding inappropriate or forbidden sexual behavior, which can cause significant distress and may lead to avoidance behaviors and checking compulsions.</li>
        <li><b>Violent Intrusive Thoughts:</b> Unwanted, intrusive thoughts or images regarding violent behavior, which can cause significant distress and may lead to avoidance and checking.</li>
        <li><b>Religious or Scrupulosity:</b> Obsessive concern with morality, sin, or blasphemy, leading to compulsive behaviors such as praying, confessing, or seeking reassurance about moral integrity.</li>
        <li><b>Relationship OCD (ROCD):</b> Persistent doubts about the suitability of a partner or the love within a relationship, leading to constant seeking of reassurance and analysis of the relationship.</li>
        <li><b>Existential OCD:</b> Obsessive contemplation about existential questions, such as the meaning of life, death, or the nature of reality, often leading to an inability to find satisfaction in answers.</li>
        <li><b>Health Anxiety OCD:</b> Obsessive concern over having or acquiring a serious illness, leading to excessive health research, checking for symptoms, and seeking reassurance.</li>
        <li><b>Perfectionism:</b> Excessive concern with making mistakes or things not being perfect, which can lead to procrastination, checking, and redoing tasks.</li>
        <li><b>Somatic OCD:</b> Obsession with bodily functions or sensations, such as breathing or blinking, leading to hyperawareness and compulsive monitoring.</li>
        <li><b>Sexual Orientation OCD (SO-OCD):</b> Obsessive doubt about one's sexual orientation, leading to compulsive behaviors aimed at seeking certainty.</li>
        <li><b>Gender Identity OCD:</b> Persistent, intrusive doubts about one's gender identity, leading to excessive rumination, research, and reassurance-seeking.</li>
      </ul>
    </div>
    <div class="footer"><span class="mark"></span><span class="brand">Calm Path</span><span class="web">www.calmpaththerapy.com</span><span class="pill">Page 07</span></div>
  </div>
  <div class="page">
    <svg class="leaf" style="right:0;top:0" width="90" height="60" viewBox="0 0 90 60" role="img" aria-label="Decorative blob"><path d="M0 0h90v50C60 70 10 50 0 0z" fill="var(--terracotta)"/></svg>
    <div class="inner">
      <h2 class="italic">The Progressive Nature of OCD:<br>How It Grows Over Time</h2>
      <p style="margin-bottom:12px">Obsessive-Compulsive Disorder (OCD) is not a static condition; it is dynamic and, without effective intervention, tends to grow more encompassing and debilitating over time. The progression of OCD can be insidious, with its impact expanding gradually, leading to a noticeable shrinkage of an individual's world and an escalation in their levels of anxiety.</p>
      <div class="card"><span class="num">01</span><div class="card-body"><div><h3>Expanding Avoidance and Restrictions:</h3><p>As OCD develops, the range of triggers for a person's obsessions and compulsions often broadens. What may start as a singular concern, such as a fear of contamination, can extend to encompass numerous aspects of daily life, including public spaces, personal interactions, and even certain thoughts or feelings. This expansion results in increasing avoidance behaviors, making the individual's world smaller and smaller. Activities and places once enjoyed become off-limits, tethering the person more tightly to their OCD.</p></div></div></div>
      <div class="card"><span class="num">02</span><div class="card-body"><div><h3>Escalating Time Commitment:</h3><p>The rituals and compulsions associated with OCD become more time-consuming as the disorder progresses. What initially may have been a brief check or a quick wash can evolve into hours-long rituals, significantly eating into the day. This escalation not only diminishes the time available for productive or enjoyable activities but also contributes to heightened stress and anxiety, as the rituals themselves become more complex and demanding.</p></div></div></div>
      <div class="card"><span class="num">03</span><div class="card-body"><div><h3>Strain on Relationships:</h3><p>The impact of OCD on relationships cannot be overlooked. The time and energy consumed by the disorder leave less room for social interactions and the nurturance of healthy relationships. Loved ones may struggle to understand or become frustrated by the compulsions and avoidance behaviors, leading to tension and conflict. Additionally, the person with OCD may withdraw from relationships out of embarrassment, guilt, or a desire to conceal their symptoms, further isolating themselves.</p></div></div></div>
      <div class="card"><span class="num">04</span><div class="card-body"><div><h3>Increasing Anxiety and Emotional Toll:</h3><p>Paradoxically, while the compulsions and avoidances of OCD are meant to control anxiety, they often serve to increase it over time. The temporary relief they provide reinforces the behavior, but the underlying anxiety not only persists—it grows. The constant battle against intrusive thoughts and the pressure of compulsions contribute to a heightened state of stress, potentially leading to other mental health issues, such as depression or anxiety disorders.</p></div></div></div>
      <div class="card"><span class="num">05</span><div class="card-body"><div><h3>Impairment in Functioning:</h3><p>As OCD intensifies, its impact can extend to all areas of life, including academic or job performance, daily routines, and overall quality of life. The disorder can become so consuming that it impairs the individual's ability to function effectively in their roles as a student, employee, partner, parent, or friend.</p></div></div></div>
    </div>
    <div class="footer"><span class="mark"></span><span class="brand">Calm Path</span><span class="web">www.calmpaththerapy.com</span><span class="pill">Page 08</span></div>
  </div>
</section>

</body>
</html>
```